CONTACT US Page and design for website

We need a contact us page for our website. We would like it to have a message area, a map, our information, etc.

Please see the text attachment for what we are looking for. We need to have something that is creative and interesting, modern and professional.

We believe that a contact US page should be very creative because everyone clicks that to contact us. We want it to be super professional, attention grabbing, pleasing to the eye.

PLEASE KEEP THE HEADER AND FOOTER THE SAME, ONLY THE ACTUAL CONTACT US PAGE NEEDS TO BE WORKED ON. THANKS!
We are excited to work with designers for this project.

Target Market(s)

Clients in technology business

Industry/Entity Type

Information Technology

Number of Pages Required

1 page

Font styles to use
Serif

Requirements
Must have
• CHECK THE TEXT ATTACHMENT PLEASE
• Must stay within our design colors and theme.
Nice to have
• see attachment
Should not have
• it should be special

```html
<!DOCTYPE html>
<html lang="en">
<head>
<meta charset="utf-8">
<title>Contact Us – Norvale Tech</title>
<link rel="stylesheet" href="https://fonts.googleapis.com/css2?family=Roboto:wght@400;500;700&display=swap">
<style>
:root{
  --teal:#2eb4a6;
  --ink:#222a30;
  --white:#ffffff;
  --panel:#f0f1f3;
  --line:#e2e4e6;
  --footer:#8d8d8d;
  --tile-grey:#8a8a8a;
  --tile-red:#b0121b;
  --tile-blue:#0a74b3;
  --tile-pink:#e5405f;
}
*{box-sizing:border-box;margin:0;padding:0}
html,body{width:758px;height:1200px;overflow:hidden}
body{position:relative;background:var(--white);font-family:"Roboto",Arial,sans-serif;color:var(--ink)}
.abs{position:absolute}

/* header */
.topbar{left:0;top:0;width:758px;height:47px;background:var(--teal)}
.crumbs{left:102px;top:17px;font-size:12px;font-weight:500;color:var(--ink)}
.crumbs .home{color:var(--white)}

/* map */
.map{left:0;top:47px;width:758px;height:320px;
  background:linear-gradient(120deg,#f5f5f2 0%,#d9d3ea 18%,#e8d98a 30%,#f2efe8 45%,#e6c66e 60%,#f4f1ea 78%,#f0d6cc 100%)}
.map-pin{left:110px;top:87px}

/* HQ card */
.hq{left:408px;top:118px;width:248px;height:179px;background:var(--teal);box-shadow:0 4px 14px rgba(0,0,0,.15);color:var(--white)}
.hq-title{position:absolute;left:0;top:27px;width:100%;text-align:center;font-size:12px;font-weight:700;letter-spacing:1.2px}
.hq-icon{position:absolute;left:59px;top:57px}
.hq-address{position:absolute;left:93px;top:58px;font-size:9px;font-weight:700;line-height:14.5px;letter-spacing:-.2px}
.hq-button{position:absolute;left:49px;top:116px;width:141px;height:31px;border:1px solid var(--white);font-size:12px;font-weight:500;letter-spacing:.4px;display:flex;align-items:center;justify-content:center}

/* hours */
.hours-title{left:102px;top:406px;font-size:15px;font-weight:500;color:var(--ink)}
.hours-rule{left:102px;top:426px;width:20px;height:2px;background:var(--teal)}
.day{width:165px;height:80px;background:var(--white);border:1px solid var(--line);box-shadow:0 1px 3px rgba(0,0,0,.06);text-align:center}
.day svg{position:absolute;left:72px;top:12px}
.day-name{position:absolute;left:0;top:43px;width:100%;font-size:9px;color:var(--ink)}
.day-hours{position:absolute;left:0;top:59px;width:100%;font-size:7.5px;color:var(--teal)}
.support{left:492px;top:562px;width:165px;height:80px;background:var(--white);border:1px solid var(--line)}
.support-icon{position:absolute;left:7px;top:20px}
.support-panel{position:absolute;left:63px;top:-1px;width:102px;height:80px;background:var(--teal);color:var(--white);text-align:center}
.support-big{margin-top:22px;font-size:15px;font-weight:700}
.support-small{margin-top:4px;font-size:8px;font-weight:700}

/* contact band */
.contact-left{left:0;top:683px;width:378px;height:395px;background:var(--teal)}
.contact-right{left:378px;top:683px;width:380px;height:395px;background:var(--panel)}
.intro{left:101px;top:724px;width:182px;font-size:11px;font-weight:700;letter-spacing:1.3px;line-height:17px;color:var(--white)}
.mini-rule{width:20px;height:1px;background:rgba(255,255,255,.8)}
.inquiry{left:101px;color:var(--white)}
.inquiry h3{font-size:11.5px;font-weight:500;letter-spacing:1.3px;margin-bottom:4px}
.inquiry p{font-size:10px;font-weight:500;letter-spacing:.8px;line-height:17px}

.tile{left:304px;width:74px;height:74px;padding-top:13px;color:var(--white);text-align:center;font-size:11px;font-weight:500;line-height:14px}
.tile .net{display:block;font-size:12px;line-height:16px;margin-bottom:6px}
.tile-1{top:730px;background:var(--tile-grey)}
.tile-2{top:804px;background:var(--tile-red)}
.tile-3{top:878px;background:var(--tile-blue)}
.tile-4{top:952px;background:var(--tile-pink)}

/* form */
.form-head{left:410px;top:732px;width:247px;height:26px;background:var(--teal);color:var(--white);font-size:12px;font-weight:500;letter-spacing:.4px;text-align:center;line-height:26px}
.form-notch{left:524px;top:758px}
.field{left:410px;width:247px;background:var(--white);border:1px solid var(--line);font-size:11px;color:#6b737a;padding-left:21px;padding-top:8px}
.field-name{top:773px;height:28px}
.field-email{top:812px;height:28px}
.field-phone{top:851px;height:28px}
.field-message{top:890px;height:98px;padding-top:12px}
.send{left:410px;top:1001px;width:247px;height:28px;background:var(--teal);color:var(--white);font-size:12px;font-weight:500;letter-spacing:.4px;display:flex;align-items:center;justify-content:center;gap:5px}

/* footer */
.footer{left:0;top:1078px;width:758px;height:122px;background:var(--footer)}
.footer-line{left:0;top:1127px;width:758px;display:flex;align-items:center;justify-content:center;gap:10px;color:var(--white);font-size:12px}
.footer-mark{width:22px;height:22px;border-radius:50%;background:rgba(255,255,255,.75)}
</style>
</head>
<body>

<header class="abs topbar"></header>
<nav class="abs crumbs"><span class="home">HOME</span> / CONTACT US</nav>

<div class="abs map" role="img" aria-label="Coloured political world map showing the office location in North America"></div>
<svg class="abs map-pin" width="40" height="60" viewBox="0 0 40 60" aria-hidden="true">
  <path d="M20 2a18 18 0 0 0-18 18c0 13 18 30 18 30s18-17 18-30A18 18 0 0 0 20 2z" fill="#fff" stroke="#2eb4a6" stroke-width="1.5"/>
  <circle cx="20" cy="20" r="7" fill="#2eb4a6"/>
  <circle cx="20" cy="55" r="3.5" fill="#2eb4a6" stroke="#fff" stroke-width="1.5"/>
</svg>

<section class="abs hq">
  <h2 class="hq-title">OFFICE HEADQUARTERS</h2>
  <svg class="hq-icon" width="26" height="30" viewBox="0 0 26 30" aria-hidden="true">
    <path d="M2 13L13 3l11 10v15H2z" fill="none" stroke="#3a3f8a" stroke-width="2" stroke-linejoin="round"/>
    <path d="M13 10a4.5 4.5 0 0 0-4.5 4.5c0 3.5 4.5 7.5 4.5 7.5s4.5-4 4.5-7.5A4.5 4.5 0 0 0 13 10z" fill="#e0287a"/>
    <circle cx="13" cy="14.5" r="1.6" fill="#fff"/>
  </svg>
  <p class="hq-address">Norvale Tech, LLC.<br>4820 Larkin Ave.<br>Westbrook, CA 90000</p>
  <div class="hq-button">Get Direction »</div>
</section>

<h2 class="abs hours-title">HOURS OF OPERATION</h2>
<div class="abs hours-rule"></div>

<div class="abs day" style="left:102px;top:452px">
  <svg width="21" height="21" viewBox="0 0 21 21" aria-hidden="true"><circle cx="10.5" cy="10.5" r="10.5" fill="#2eb4a6"/><path d="M6 11l3 3 6-6" fill="none" stroke="#fff" stroke-width="2.2" stroke-linecap="round" stroke-linejoin="round"/></svg>
  <div class="day-name">Monday</div><div class="day-hours">8:00am- 5:00pm</div>
</div>
<div class="abs day" style="left:297px;top:452px">
  <svg width="21" height="21" viewBox="0 0 21 21" aria-hidden="true"><circle cx="10.5" cy="10.5" r="10.5" fill="#2eb4a6"/><path d="M6 11l3 3 6-6" fill="none" stroke="#fff" stroke-width="2.2" stroke-linecap="round" stroke-linejoin="round"/></svg>
  <div class="day-name">Tuesday</div><div class="day-hours">8:00am- 5:00pm</div>
</div>
<div class="abs day" style="left:492px;top:452px">
  <svg width="21" height="21" viewBox="0 0 21 21" aria-hidden="true"><circle cx="10.5" cy="10.5" r="10.5" fill="#2eb4a6"/><path d="M6 11l3 3 6-6" fill="none" stroke="#fff" stroke-width="2.2" stroke-linecap="round" stroke-linejoin="round"/></svg>
  <div class="day-name">Wednesday</div><div class="day-hours">8:00am- 5:00pm</div>
</div>
<div class="abs day" style="left:102px;top:562px">
  <svg width="21" height="21" viewBox="0 0 21 21" aria-hidden="true"><circle cx="10.5" cy="10.5" r="10.5" fill="#2eb4a6"/><path d="M6 11l3 3 6-6" fill="none" stroke="#fff" stroke-width="2.2" stroke-linecap="round" stroke-linejoin="round"/></svg>
  <div class="day-name">Thursday</div><div class="day-hours">8:00am- 5:00pm</div>
</div>
<div class="abs day" style="left:297px;top:562px">
  <svg width="21" height="21" viewBox="0 0 21 21" aria-hidden="true"><circle cx="10.5" cy="10.5" r="10.5" fill="#2eb4a6"/><path d="M6 11l3 3 6-6" fill="none" stroke="#fff" stroke-width="2.2" stroke-linecap="round" stroke-linejoin="round"/></svg>
  <div class="day-name">Friday</div><div class="day-hours">8:00am- 5:00pm</div>
</div>
<div class="abs support">
  <svg class="support-icon" width="50" height="42" viewBox="0 0 50 42" aria-hidden="true">
    <circle cx="22" cy="20" r="17" fill="#4ec9ea" stroke="#1f2a3a" stroke-width="2"/>
    <circle cx="22" cy="20" r="12" fill="#fff"/>
    <path d="M22 11v9l6 3" fill="none" stroke="#1f2a3a" stroke-width="2" stroke-linecap="round"/>
    <circle cx="22" cy="20" r="2" fill="#1f2a3a"/>
    <text x="29" y="40" font-family="Roboto,Arial,sans-serif" font-size="14" fill="#1f2a3a">24</text>
  </svg>
  <div class="support-panel">
    <div class="support-big">24/7 Hrs</div>
    <div class="support-small">Dedicated support</div>
  </div>
</div>

<section class="abs contact-left"></section>
<section class="abs contact-right"></section>

<p class="abs intro">We'd love to hear from you! Send us a message using the form opposite, or email us</p>
<div class="abs mini-rule" style="left:101px;top:797px"></div>

<div class="abs inquiry" style="top:816px">
  <h3>General Inquiries</h3>
  <p>(555)010-3013<br>info@norvaletech.com</p>
</div>
<div class="abs mini-rule" style="left:101px;top:874px"></div>

<div class="abs inquiry" style="top:896px">
  <h3>Sales Inquiries</h3>
  <p>(555)010-3013<br>sales@norvaletech.com</p>
</div>
<div class="abs mini-rule" style="left:101px;top:954px"></div>

<div class="abs inquiry" style="top:975px">
  <h3>Purchasing Inquiries</h3>
  <p>(555)010-3014<br>purchasing@norvaletech.com</p>
</div>
<div class="abs mini-rule" style="left:101px;top:1034px"></div>

<div class="abs tile tile-1"><span class="net">Murmur</span>Fans<br>5,500</div>
<div class="abs tile tile-2"><span class="net">Orbit</span>Friends<br>5,100</div>
<div class="abs tile tile-3"><span class="net">Netlink</span>Followers<br>3,900</div>
<div class="abs tile tile-4"><span class="net">Picto</span>Friends<br>5,900</div>

<div class="abs form-head">Get in Touch</div>
<svg class="abs form-notch" width="16" height="9" viewBox="0 0 16 9" aria-hidden="true"><path d="M0 0h16L8 9z" fill="#2eb4a6"/></svg>
<div class="abs field field-name">Your Name*</div>
<div class="abs field field-email">Email*</div>
<div class="abs field field-phone">Phone*</div>
<div class="abs field field-message">Your Message*</div>
<div class="abs send">Send <svg width="6" height="8" viewBox="0 0 6 8" aria-hidden="true"><path d="M0 0l6 4-6 4z" fill="#fff"/></svg></div>

<footer class="abs footer"></footer>
<div class="abs footer-line"><span class="footer-mark"></span><span>NORVALE TECH, LLC.COPYRIGHT © 2017</span></div>

</body>
</html>
```